Floral Design for Weddings And Events

I create floral designs for weddings and events. I create unusual designs that people will remember.

Industry/Entity Type

Floral

Contact Information for Business Card

Reeds
Weddings and Events
Marlene Dukov, owner/designer
2817 Corvell Ln
San Marcos, CA 92078
marlyduknv@mailbrook.net
412 736-2185

Requirements
Must have
• I would like the name of the business, REEDS, to Stand Out!! I like clean, bold lines.. nothing foo-foo! Must be easy to read I'm looking for a design that catches your eye and represents my creativity. I want my card to show the potential customer that I'm unique and creative
Nice to have
• I'm thinking of the name REEDS maybe worked into the design... I'm open to your creative ideas!!!! The name must be very legible
Should not have
• I'm open to any colors other that pink and yellow..nothing Foo-Foo or flowery..

```html
<!DOCTYPE html>
<html lang="en">
<head>
<meta charset="utf-8">
<title>Reeds – Business Card</title>
<link href="https://fonts.googleapis.com/css2?family=Montserrat:wght@400;700;800&display=swap" rel="stylesheet">
<style>
  :root {
    --backdrop: #e6e6e3;
    --accent: #6cc3b6;
    --accent-soft: #a9d9d1;
    --white: #ffffff;
    --band-grey: #2e2e2e;
    --text-muted: #c4cccb;
  }
  html, body {
    margin: 0;
    width: 1200px;
    height: 800px;
    overflow: hidden;
    background: var(--backdrop);
    font-family: "Montserrat", Arial, sans-serif;
  }
  .card {
    position: absolute;
    left: 110px;
    top: 120px;
    width: 980px;
    height: 560px;
    overflow: hidden;
    box-shadow: 0 18px 40px rgba(0,0,0,.25);
  }
  .card-art { position: absolute; inset: 0; }
  .brand {
    position: absolute;
    left: 390px;
    top: 48px;
    margin: 0;
    color: var(--accent);
    font-weight: 700;
    font-size: 124px;
    line-height: 1;
    letter-spacing: 1px;
  }
  .tagline {
    position: absolute;
    left: 548px;
    top: 186px;
    color: var(--white);
    font-weight: 400;
    font-size: 25px;
  }
  .person-name {
    position: absolute;
    left: 58px;
    top: 240px;
    margin: 0;
    color: var(--accent);
    font-weight: 800;
    font-size: 36px;
    line-height: 1;
    letter-spacing: 1px;
  }
  .person-role {
    position: absolute;
    left: 40px;
    top: 280px;
    color: var(--white);
    font-size: 21px;
    line-height: 1;
  }
  .contact-list {
    position: absolute;
    left: 40px;
    top: 336px;
    margin: 0;
    padding: 0;
    list-style: none;
  }
  .contact-item {
    display: flex;
    align-items: center;
    gap: 18px;
    height: 34px;
    color: var(--accent);
    font-size: 20px;
  }
  .contact-icon { width: 18px; height: 18px; flex: none; }
  .address {
    position: absolute;
    right: 44px;
    top: 438px;
    color: var(--text-muted);
    font-size: 20px;
  }
</style>
</head>
<body>
  <div class="card">
    <svg class="card-art" width="980" height="560" viewBox="0 0 980 560">
      <defs>
        <linearGradient id="cardShade" x1="0" y1="0" x2="1" y2="1">
          <stop offset="0" stop-color="#0b0b0b"/>
          <stop offset="0.55" stop-color="#242424"/>
          <stop offset="1" stop-color="#4a4a4a"/>
        </linearGradient>
      </defs>
      <rect class="card-face" width="980" height="560" fill="url(#cardShade)"/>
      <polygon class="band-grey" points="0,486 345,486 372,512 372,560 0,560" fill="var(--band-grey)"/>
      <polyline class="band-rule" points="0,484 344,484 371,510" fill="none" stroke="var(--white)" stroke-width="4"/>
      <rect class="band-accent" x="372" y="506" width="608" height="54" fill="var(--accent)"/>
      <line class="name-rule" x1="150" y1="318" x2="980" y2="318" stroke="var(--accent)" stroke-width="2"/>
    </svg>

    <h1 class="brand">Reeds</h1>
    <div class="tagline">Weddings and Events</div>

    <h2 class="person-name">MARLENE DUKOV</h2>
    <div class="person-role">owner</div>

    <ul class="contact-list">
      <li class="contact-item">
        <svg class="contact-icon" viewBox="0 0 18 18"><circle cx="9" cy="5" r="4" fill="#fff"/><path d="M1 18c0-5 3.5-7 8-7s8 2 8 7z" fill="#fff"/></svg>
        412 736-2185
      </li>
      <li class="contact-item">
        <svg class="contact-icon" viewBox="0 0 18 18"><rect x="1" y="3" width="16" height="12" fill="none" stroke="#fff" stroke-width="1.6"/><path d="M1 3l8 7 8-7" fill="none" stroke="#fff" stroke-width="1.6"/></svg>
        marlyduknv@mailbrook.net
      </li>
      <li class="contact-item">
        <svg class="contact-icon" viewBox="0 0 18 18"><circle cx="9" cy="9" r="8" fill="none" stroke="#fff" stroke-width="1.6"/><ellipse cx="9" cy="9" rx="3.5" ry="8" fill="none" stroke="#fff" stroke-width="1.2"/><line x1="1" y1="9" x2="17" y2="9" stroke="#fff" stroke-width="1.2"/></svg>
        www.reedsfloral.net
      </li>
    </ul>

    <div class="address">2817 Corvell Ln San Marcos, CA 92078</div>
  </div>
</body>
</html>
```